Services Brochure

We need an revised brochure for our 3 main services. I have uploaded our old Brochure for reference. We have 3 main services (Managed IT Services, Business VoIP, Business Internet). Below is some text we would like included in the brochure for each service section. In addition I have attached a "mock up" showing that we want IT Services on top, VoIP in the middle and Internet at the bottom. Please use your design experience to select images that would fit well. I also included an image of the phone we would like to use.
Text for Brochure:
Title/Header: Unleash the Power of Local IT Solutions
IT Services That Mean Business
Experience fanatical customer service with our affordable, full-service IT solutions. We’re 100% local, ensuring leading response times and personalized support—so you can focus on what you do best.
Talk More, Worry Less with Our Telephone Services
Say goodbye to overpriced equipment and hello to our free phone plan. Keep your number and enjoy unlimited local and long-distance calling. Tailor your phone system to your business needs and rest assured—our rates are always the lowest in town.
Highspeed Internet That Sets You Apart
Stay connected with blazing-fast speeds—from 1Gbps to 10Gbps, both up and down. Benefit from a static IP address and unbeatable prices, backed by 100% local support. Get the connectivity your business deserves at the best value in town.
Elevate your business with cutting-edge technology.
Sorry everyone the banner size is 81" high and 33" wide.

```html
<!DOCTYPE html>
<html lang="en">
<head>
<meta charset="UTF-8">
<title>Corvane – Local IT Solutions</title>
<link href="https://fonts.googleapis.com/css2?family=Poppins:wght@300;400;600;700;800&family=Tinos:ital,wght@1,700&display=swap" rel="stylesheet">
<style>
  :root {
    --page-bg: #9a9eab;
    --paper: #ffffff;
    --brand-blue: #10208a;
    --header-blue: #1a33b0;
    --header-deep: #0c1f8f;
    --wedge-gray: #858585;
    --body-gray: #555a66;
    --accent-orange: #df8a1c;
  }
  * { margin: 0; padding: 0; box-sizing: border-box; }
  html, body { width: 1068px; height: 1200px; overflow: hidden; }
  body { background: var(--page-bg); font-family: "Poppins", sans-serif; position: relative; }

  .flyer {
    position: absolute; left: 144px; top: 15px;
    width: 950px; height: 1425px;
    transform: scale(0.821); transform-origin: top left;
    background: var(--paper);
    box-shadow: 0 2px 6px rgba(0,0,0,0.25);
    overflow: hidden;
  }

  .hero { position: absolute; left: 0; top: 0; width: 950px; height: 467px; }
  .hero-shapes { position: absolute; inset: 0; width: 100%; height: 100%; }
  .hero-title {
    position: absolute; left: 67px; top: 148px;
    color: #fff; line-height: 86px; white-space: nowrap;
  }
  .hero-title .light { font-weight: 300; font-size: 70px; display: block; letter-spacing: 0.5px; }
  .hero-title .bold { font-weight: 800; font-size: 72px; display: block; text-shadow: 0 3px 6px rgba(0,0,0,0.35); }

  .brand-name {
    position: absolute; right: 60px; top: 62px;
    font-weight: 700; font-size: 92px; line-height: 1;
    color: var(--brand-blue); letter-spacing: -2px;
  }

  .service { position: absolute; left: 37px; width: 880px; }
  .service-media {
    position: absolute; left: 0; top: 0; width: 305px; height: 190px;
    background: #fff; border-radius: 16px;
    box-shadow: 0 0 0 1px #e6e6ea, 0 2px 6px rgba(0,0,0,0.12);
  }
  .service-media .photo { position: absolute; inset: 8px; border-radius: 12px; }
  .photo-it { background: radial-gradient(circle at 50% 55%, #1e8c8a, #0a3236 60%, #061b1e); }
  .photo-phone { background: linear-gradient(135deg, #ececee, #cfcfd3 50%, #e9e9eb); }
  .photo-internet { background: linear-gradient(90deg, #1a2bd0, #6a4ee0 35%, #e66ab8 55%, #2a6ae8 80%, #0d1a9a); }

  .service-text { position: absolute; left: 332px; top: 6px; width: 518px; }
  .service-text h2 {
    color: var(--brand-blue); font-weight: 600; font-size: 30px; line-height: 36px;
    margin-bottom: 6px;
  }
  .service-text p { color: var(--body-gray); font-weight: 400; font-size: 19.5px; line-height: 29.6px; }

  .service-it { top: 532px; }
  .service-voice { top: 764px; }
  .service-internet { top: 1024px; }

  .tagline {
    position: absolute; left: 0; right: 0; top: 1280px; text-align: center;
    font-family: "Tinos", serif; font-style: italic; font-weight: 700;
    font-size: 35px; color: var(--accent-orange);
  }

  .contact-row {
    position: absolute; left: 24px; right: 24px; top: 1357px;
    display: flex; align-items: center; justify-content: space-between;
  }
  .contact-item { display: flex; align-items: center; white-space: nowrap; }
  .contact-icon {
    width: 39px; height: 39px; border-radius: 4px; background: var(--brand-blue);
    display: flex; align-items: center; justify-content: center; margin-right: 8px;
    flex: none;
  }
  .contact-item span { font-size: 28px; color: var(--body-gray); font-weight: 400; }
</style>
</head>
<body>
  <div class="flyer">
    <header class="hero">
      <svg class="hero-shapes" viewBox="0 0 950 467" preserveAspectRatio="none" role="img" aria-label="Blue technology background with circuit and gear graphics">
        <defs>
          <radialGradient id="heroGlow" cx="0.45" cy="0.6" r="0.7">
            <stop offset="0" stop-color="#2a4cd6"/>
            <stop offset="1" stop-color="#0c1f8f"/>
          </radialGradient>
          <linearGradient id="whiteFade" x1="0" y1="0" x2="1" y2="0.6">
            <stop offset="0" stop-color="#dfe2ee"/>
            <stop offset="0.35" stop-color="#ffffff"/>
          </linearGradient>
        </defs>
        <rect width="950" height="467" fill="url(#heroGlow)"/>
        <polygon points="295,0 950,0 950,440" fill="url(#whiteFade)"/>
        <polygon points="950,210 775,322 950,452" fill="var(--wedge-gray)"/>
      </svg>
      <div class="brand-name">corvane</div>
      <h1 class="hero-title">
        <span class="light">Unleash</span>
        <span class="light">The Power of</span>
        <span class="bold">Local IT Solutions</span>
      </h1>
    </header>

    <section class="service service-it">
      <div class="service-media"><div class="photo photo-it" role="img" aria-label="Person touching a glowing holographic tech interface"></div></div>
      <div class="service-text">
        <h2>IT Services That Mean Business</h2>
        <p>Experience fanatical customer service with our affordable, full-service IT solutions. We’re 100% local, ensuring leading response times and personalized support—so you can focus on what you do best.</p>
      </div>
    </section>

    <section class="service service-voice">
      <div class="service-media"><div class="photo photo-phone" role="img" aria-label="Desk IP phone with colour display on a light background"></div></div>
      <div class="service-text">
        <h2>Talk More, Worry Less with<br>Our Telephone Services</h2>
        <p>Say goodbye to overpriced equipment and hello to our free phone plan. Keep your number and enjoy unlimited local and long-distance calling. Tailor your phone system to your business needs and rest assured—our rates are always the lowest in town.</p>
      </div>
    </section>

    <section class="service service-internet">
      <div class="service-media"><div class="photo photo-internet" role="img" aria-label="Figure racing through light streaks with a Wi-Fi symbol"></div></div>
      <div class="service-text">
        <h2>Highspeed Internet That Sets<br>You Apart</h2>
        <p>Stay connected with blazing-fast speeds—from 1Gbps to 10Gbps, both up and down. Benefit from a static IP address and unbeatable prices, backed by 100% local support. Get the connectivity your business deserves at the best value in town.</p>
      </div>
    </section>

    <p class="tagline">Elevate your business with cutting-edge technology</p>

    <footer class="contact-row">
      <div class="contact-item">
        <div class="contact-icon">
          <svg width="24" height="24" viewBox="0 0 24 24"><path d="M6.6 3.5l2.6 3.2-1.5 2c1 2.2 2.9 4.1 5.1 5.1l2-1.5 3.2 2.6-1.4 3.1C10.5 18 6 13.5 3.5 7.4z" fill="#fff"/><path d="M14 4a6 6 0 0 1 6 6M14 7.5a2.5 2.5 0 0 1 2.5 2.5" stroke="#fff" stroke-width="1.6" fill="none"/></svg>
        </div>
        <span>509-555-0142</span>
      </div>
      <div class="contact-item">
        <div class="contact-icon">
          <svg width="24" height="24" viewBox="0 0 24 24"><rect x="3" y="6" width="18" height="12" fill="none" stroke="#fff" stroke-width="1.8"/><path d="M3 6l9 7 9-7" fill="none" stroke="#fff" stroke-width="1.8"/></svg>
        </div>
        <span>sales@corvane.com</span>
      </div>
      <div class="contact-item">
        <div class="contact-icon">
          <svg width="24" height="24" viewBox="0 0 24 24" fill="none" stroke="#fff" stroke-width="1.5"><circle cx="12" cy="12" r="8.5"/><ellipse cx="12" cy="12" rx="3.8" ry="8.5"/><path d="M3.5 12h17M5 8h14M5 16h14"/></svg>
        </div>
        <span>www.corvane.com</span>
      </div>
    </footer>
  </div>
</body>
</html>
```